Midwife Poster Ad

I need a poster to go on a wall in my clinic which is in a medical centre shared by doctors and other health professionals. I am a self-employed midwife in New Zealand. I hope for this poster to catch some of the many women who come into the medical centre to have pregnancy tests, see a doctor, or use the pregnancy yoga/pilates services also offered. It will be going on a wall with a bunch of other brochures and ads, so obviously I would like it to stand out and grab their attention as they walk in or out of the centre.

I have attached a few of the images that I currently use in my business cards and brochures. I would like my portrait to feature somewhere on the poster, but does not need to be central. The other images can be used if they work with the design, but are not essential. I would like the poster to include at least one image of a new baby or a pregnant woman/couple.

I would also like a small business card-sized space at the bottom where I can attach a card-holder. I would like the website address to stand out.

The poster should be colourful and communicate the excitement of a new pregnancy.

Target Market(s)

Pregnant women, mothers

Industry/Entity Type

Small Business

Requirements
Must have
• The poster needs to include the following text:
EXPECTING A BABY?
Midwife available here!
Marlene Tobbit LMC Midwife
Clinics run from Kestrel Physio & Pilates
Free pregnancy testing
www.brindlewoodmidwife.co.nz
0215379064

```html
<!DOCTYPE html>
<html lang="en">
<head>
<meta charset="utf-8">
<title>Expecting a Baby? – Midwife Poster</title>
<link rel="stylesheet" href="https://fonts.googleapis.com/css2?family=Bebas+Neue&family=Raleway:wght@300&display=swap">
<style>
  :root {
    --pink: #e292ab;
    --grey-band: #a9a9ab;
    --grey-text: #b1b1b3;
    --white: #ffffff;
    --tile-pink: #e08fa9;
    --tile-blue: #b6e0ea;
    --tile-green: #b3dba7;
    --tile-lilac: #d5a9d6;
  }
  html, body {
    margin: 0;
    padding: 0;
    overflow: hidden;
    background: var(--white);
  }
  .poster {
    width: 848px;
    height: 1200px;
    position: relative;
    overflow: hidden;
    background: var(--white);
  }
  .poster svg { display: block; }
  .band-pink { fill: var(--pink); }
  .band-grey { fill: var(--grey-band); }
  .headline {
    font-family: "Bebas Neue", "Oswald", sans-serif;
    fill: var(--white);
    font-size: 196px;
  }
  .details {
    font-family: "Raleway", sans-serif;
    font-weight: 300;
    fill: var(--white);
    font-size: 28px;
    font-variant-numeric: lining-nums;
  }
  .contact {
    font-family: "Raleway", sans-serif;
    font-weight: 300;
    fill: var(--grey-text);
    font-size: 56px;
    font-variant-numeric: lining-nums;
  }
  .frame { fill: var(--white); }
  .tile-pink { fill: var(--tile-pink); }
  .tile-blue { fill: var(--tile-blue); }
  .tile-green { fill: var(--tile-green); }
  .tile-lilac { fill: var(--tile-lilac); }
</style>
</head>
<body>
<main class="poster">
  <svg width="848" height="1200" viewBox="0 0 848 1200" xmlns="http://www.w3.org/2000/svg">
    <defs>
      <linearGradient id="portrait-tone" x1="0" y1="0" x2="0" y2="1">
        <stop offset="0" stop-color="#3f5b35"/>
        <stop offset="0.55" stop-color="#b98a70"/>
        <stop offset="1" stop-color="#1f2030"/>
      </linearGradient>
      <linearGradient id="father-baby-tone" x1="0" y1="0" x2="1" y2="1">
        <stop offset="0" stop-color="#3a3a3a"/>
        <stop offset="0.5" stop-color="#9a9a9a"/>
        <stop offset="1" stop-color="#1c1c1c"/>
      </linearGradient>
      <linearGradient id="basket-baby-tone" x1="0" y1="0" x2="1" y2="1">
        <stop offset="0" stop-color="#9e1218"/>
        <stop offset="0.6" stop-color="#c54a3a"/>
        <stop offset="1" stop-color="#e8d8cc"/>
      </linearGradient>
      <linearGradient id="sleeping-baby-tone" x1="0" y1="0" x2="1" y2="1">
        <stop offset="0" stop-color="#b5231f"/>
        <stop offset="0.5" stop-color="#e2b096"/>
        <stop offset="1" stop-color="#f1c9b0"/>
      </linearGradient>
      <linearGradient id="couple-tone" x1="0" y1="0" x2="1" y2="1">
        <stop offset="0" stop-color="#111111"/>
        <stop offset="0.55" stop-color="#7a5a4a"/>
        <stop offset="1" stop-color="#151515"/>
      </linearGradient>
    </defs>

    <!-- Bands -->
    <polygon class="band-grey" points="0,442 848,374 848,596 0,662"/>
    <polygon class="band-pink" points="0,0 848,0 848,366 0,432"/>

    <!-- Headline -->
    <g class="headline">
      <text transform="translate(34 236) rotate(-4.7)" x="0" y="0" textLength="794" lengthAdjust="spacingAndGlyphs">EXPECTING A</text>
      <text transform="translate(258 372) rotate(-4.7)" x="0" y="0" textLength="408" lengthAdjust="spacingAndGlyphs">BABY?</text>
    </g>

    <!-- Portrait -->
    <g transform="rotate(-2 140 492)">
      <rect class="frame" x="28" y="342" width="226" height="300"/>
      <rect x="40" y="354" width="202" height="276" fill="url(#portrait-tone)" role="img" aria-label="Portrait photo of the midwife"/>
    </g>

    <!-- Details -->
    <g class="details" text-anchor="end" transform="rotate(-4.5 816 510)">
      <text x="816" y="462">Midwife available here!</text>
      <text x="816" y="498">Marlene Tobbit LMC Midwife</text>
      <text x="816" y="534">Clinics run from Kestrel Physio &amp; Pilates</text>
      <text x="816" y="570">Free pregnancy testing</text>
    </g>

    <!-- Tile grid -->
    <rect class="tile-pink" x="21" y="669" width="198" height="198" transform="rotate(-4 120 768)"/>
    <rect x="221" y="648" width="198" height="198" fill="url(#father-baby-tone)" transform="rotate(-4 320 747)" role="img" aria-label="Black and white photo of a father holding a newborn"/>
    <rect class="tile-blue" x="424" y="636" width="198" height="198" transform="rotate(-4 523 735)"/>
    <rect x="626" y="621" width="198" height="198" fill="url(#basket-baby-tone)" transform="rotate(-4 725 720)" role="img" aria-label="Photo of a newborn lying in a woven basket on red"/>
    <rect x="21" y="867" width="198" height="198" fill="url(#sleeping-baby-tone)" transform="rotate(-4 120 966)" role="img" aria-label="Photo of a sleeping newborn on a red background"/>
    <rect class="tile-green" x="225" y="855" width="198" height="198" transform="rotate(-4 324 954)"/>
    <rect x="427" y="837" width="198" height="198" fill="url(#couple-tone)" transform="rotate(-4 526 936)" role="img" aria-label="Photo of an expecting couple holding the pregnant belly"/>
    <rect class="tile-lilac" x="631" y="819" width="198" height="198" transform="rotate(-4 730 918)"/>

    <!-- Contact -->
    <g class="contact">
      <text transform="translate(96 1136) rotate(-4.7)" x="0" y="0" textLength="664" lengthAdjust="spacingAndGlyphs">www.brindlewoodmidwife.co.nz</text>
      <text transform="translate(316 1180) rotate(-4.5)" x="0" y="0" textLength="250" lengthAdjust="spacingAndGlyphs">0215379064</text>
    </g>
  </svg>
</main>
</body>
</html>
```